Brindle and Fern LLC | Land Clearing, Landscaping & Dump Trailer Services

Project Description: Brindle and Fern LLC Website Design
The website will be published using squarespace
Objective:
Design a visually compelling and conversion-driven website for Brindle and Fern LLC, a land solutions business based in Pickens County, Georgia. The site will highlight the company’s professionalism, locally rooted service, and commitment to quality in land clearing, grading, and dump trailer services.
Pages & Features to Include:
1. Landing Page (Homepage)
- Clear tagline: Sculpting Land with Precision and Power
- Call-to-Action (CTA) buttons: “Get a Free Quote” and “View Services”
- Service highlights with icons or photos (e.g., grading, mulching, hauling)
- Customer testimonials
- Embedded contact form
- Google Maps integration showing service area
2. Services + Pricing Page
- Organized list of services under 3 categories:
- **Land Clearing & Grading**
- Forestry Mulching
- Gravel Driveway Repair
- Minimum Job Fee:
- Dump Trailer Services
- Trailer Rental (Daily):
- Junk Removal (Full Load)
- Material Delivery: $ + mileage
- Specialty Jobs
- Stump removal, light demolition
- Each service section includes short descriptions and photos
- Optional quote form at the bottom with “Request a Quote” CTA
Design Style:
- Clean, professional design using clean tones
- Fonts that balance industrial strength and local charm
- Mobile-optimized with fast loading speeds and easy navigation
- SEO-optimized for terms like *land clearing Pickens County*, *grading services North Georgia*, and *dump trailer rental Jasper GA*, etc...

```html
<!DOCTYPE html>
<html lang="en">
<head>
<meta charset="utf-8">
<title>Brindle and Fern LLC | Land Clearing, Grading &amp; Dump Trailer Services</title>
<link rel="stylesheet" href="https://fonts.googleapis.com/css2?family=Poppins:wght@300;400;500;600;700&display=swap">
<style>
:root{
  --green:#4a9634;
  --green-dark:#3f852b;
  --green-pale:#eaf2df;
  --green-band:#d9ecc7;
  --navy:#323f52;
  --ink:#222a33;
  --text:#3b3b3b;
  --muted:#666;
  --grey-bg:#f3f3f3;
  --footer:#16200f;
  --white:#fff;
  --star:#f3a712;
}
*{box-sizing:border-box;margin:0;padding:0}
html,body{width:1200px;height:3555px;overflow:hidden}
body{position:relative;font-family:"Poppins",sans-serif;color:var(--text);background:var(--white)}
.abs{position:absolute}
.green{color:var(--green)}

/* top bar */
.topbar{left:469px;top:0;width:731px;height:32px;background:var(--green-band)}
.topbar .social{position:absolute;left:60px;top:10px;display:flex;gap:18px}
.topbar .social span{width:11px;height:11px;background:var(--ink);border-radius:2px}
.topbar .contact{position:absolute;top:7px;font-size:13px;color:var(--ink);display:flex;align-items:center;gap:8px;white-space:nowrap}

/* hero */
.hero-shape{left:21px;top:55px}
.brand{left:145px;top:80px;display:flex;align-items:center;gap:10px;font-weight:700;font-size:20px;color:var(--ink);line-height:1.1;width:230px}
.brand .mark{width:22px;height:22px;background:var(--green);flex:none}
.nav{top:86px;font-size:15px;color:var(--white)}
.btn{display:flex;align-items:center;justify-content:center;font-weight:500;border-radius:4px}
.btn-green{background:var(--green);color:var(--white)}
.btn-white{background:var(--white);color:var(--green)}
.hero-img{left:699px;top:143px;width:451px;height:447px;border-radius:12px;background:linear-gradient(160deg,#2c5f86 0%,#c98b4f 45%,#e5a35c 60%,#7a4a25 85%,#4a2c17 100%)}
.hero-title{left:141px;top:248px;color:var(--white);font-size:47px;line-height:60px;font-weight:400}
.hero-title b{font-weight:700;font-size:48px}
.hero-text{left:141px;top:386px;width:440px;color:var(--white);font-size:16px;line-height:25px;font-weight:300}
.avatars{left:141px;top:541px;display:flex}
.avatars span{width:40px;height:40px;border-radius:50%;border:2px solid var(--white);margin-right:-14px;background:linear-gradient(135deg,#b65a4a,#e0a84d)}
.trust{left:239px;top:546px;color:var(--white);font-size:11.5px;line-height:17px}

/* services */
.eyebrow{font-size:16px;color:var(--muted)}
.section-title{font-size:31px;font-weight:700;color:var(--ink);letter-spacing:.3px}
.card{top:832px;width:289px;height:351px;background:var(--white);box-shadow:0 2px 14px rgba(0,0,0,.09)}
.card .photo{position:absolute;left:0;top:0;width:289px;height:190px}
.card .tab{position:absolute;left:20px;top:168px;width:249px;height:44px;background:var(--white);box-shadow:0 2px 8px rgba(0,0,0,.06);display:flex;align-items:center;justify-content:center;font-weight:500;font-size:16px;color:var(--ink)}
.card p{position:absolute;left:22px;top:234px;width:245px;text-align:center;font-size:13.3px;line-height:21.5px;color:var(--text)}
.card .go{position:absolute;left:129px;top:338px;width:31px;height:31px;border:1.5px solid var(--green);background:var(--white);border-radius:3px;display:flex;align-items:center;justify-content:center}

/* testimonials */
.testi-band{left:0;top:1366px;width:1200px;height:528px;background:var(--grey-bg)}
.t-card{top:1543px;width:445px;height:238px;background:var(--white)}
.t-card .face{position:absolute;left:21px;top:35px;width:86px;height:86px;border-radius:50%;background:linear-gradient(180deg,#d9d9d9,#a9a9a9)}
.t-card .name{position:absolute;left:135px;top:45px;font-size:16px;font-weight:500;color:var(--ink)}
.t-card .stars{position:absolute;right:28px;top:44px;color:var(--star);font-size:14px;letter-spacing:1px}
.t-card p{position:absolute;left:135px;top:76px;width:290px;font-size:15px;line-height:21px;color:var(--text)}
.t-card .quote{position:absolute;left:40px;top:158px}
.arrow{width:35px;height:35px;border-radius:3px;display:flex;align-items:center;justify-content:center}

/* contact */
.form-box{left:141px;top:1982px;width:459px;height:589px;background:var(--green)}
.form-box h2{position:absolute;left:0;top:48px;width:100%;text-align:center;font-size:31px;font-weight:700;color:var(--white)}
.form-box h2 span{color:var(--ink)}
.field{position:absolute;left:29px;width:402px;border:1px solid rgba(255,255,255,.85);border-radius:5px}
.field label{position:absolute;left:10px;top:-9px;background:var(--green);padding:0 3px;font-size:12.5px;color:var(--white)}
.field .val{position:absolute;left:13px;top:12px;font-size:13.5px;color:var(--white)}
.submit{position:absolute;left:29px;top:491px;width:402px;height:41px;background:var(--white);border-radius:3px;display:flex;align-items:center;justify-content:center;font-size:13px;color:var(--ink);font-weight:500}
.cta-box{left:600px;top:2080px;width:459px;height:393px;background:var(--green-pale)}
.cta-box h3{position:absolute;left:37px;top:98px;font-size:25px;line-height:34px;font-weight:600;color:var(--ink)}
.cta-box p{position:absolute;left:37px;top:181px;width:390px;font-size:13px;line-height:23px;color:var(--ink)}

/* map */
.map{left:0;top:2659px;width:1200px;height:494px;background:linear-gradient(135deg,#dfeee0 0%,#e7f0dd 40%,#d7e9d6 70%,#e4eedc 100%)}
.map-title{left:401px;top:2696px;width:396px;height:68px;background:var(--white);border-radius:4px;display:flex;align-items:center;justify-content:center;font-size:31px;font-weight:700;color:var(--ink)}

/* footer */
.footer{left:0;top:3153px;width:1200px;height:361px;background:var(--footer)}
.f-brand{left:142px;top:3305px;display:flex;align-items:center;gap:12px;font-size:24px;font-weight:700;color:var(--white);width:200px;line-height:1.15}
.f-brand .mark{width:24px;height:24px;background:var(--white);flex:none}
.f-head{top:3231px;font-size:16px;font-weight:600;color:var(--white)}
.f-link{font-size:13.5px;color:var(--white)}
.f-soc{display:flex;align-items:center;gap:8px;font-size:13.5px;color:var(--white)}
.f-soc i{width:27px;height:27px;border:1px solid var(--white);border-radius:3px;display:flex;align-items:center;justify-content:center}
.f-soc i b{width:9px;height:9px;background:var(--white)}
.f-ct{display:flex;gap:10px;font-size:13.5px;line-height:18px;color:var(--white)}
.f-ct i{width:28px;height:28px;border:1px solid var(--white);border-radius:3px;display:flex;align-items:center;justify-content:center;flex:none}
.copy{left:0;top:3514px;width:1200px;height:41px;background:var(--green);display:flex;align-items:center;justify-content:center;font-size:12px;color:var(--white)}
</style>
</head>
<body>

<!-- top bar -->
<div class="abs topbar">
  <div class="social"><span></span><span></span><span></span><span></span></div>
  <div class="contact" style="left:230px"><svg width="11" height="8" viewBox="0 0 11 8"><rect width="11" height="8" fill="#222a33"/></svg>info@brindleandfernllc.com</div>
  <div class="contact" style="left:472px"><svg width="11" height="11" viewBox="0 0 24 24"><path fill="#222a33" d="M6.6 10.8a15 15 0 0 0 6.6 6.6l2.2-2.2c.3-.3.7-.4 1-.2 1.1.4 2.3.6 3.6.6.6 0 1 .4 1 1V20c0 .6-.4 1-1 1A17 17 0 0 1 3 4c0-.6.4-1 1-1h3.5c.6 0 1 .4 1 1 0 1.3.2 2.5.6 3.6.1.3 0 .7-.2 1z"/></svg>(123) 456-7890</div>
</div>

<!-- hero -->
<svg class="abs hero-shape" width="1158" height="563" viewBox="0 0 1158 563">
  <path fill="#323f52" d="M20 111H300Q312 111 318 101L372 10Q378 0 390 0H1138Q1158 0 1158 20V543Q1158 563 1138 563H20Q0 563 0 543V131Q0 111 20 111Z"/>
</svg>
<div class="abs brand"><span class="mark"></span>Brindle and Fern LLC</div>
<div class="abs nav" style="left:723px;font-weight:600">Home</div>
<div class="abs nav" style="left:829px">Service</div>
<div class="abs btn btn-green" style="left:945px;top:73px;width:113px;height:41px;font-size:13px">Contact Us</div>
<div class="abs hero-img" role="img" aria-label="Excavator digging into earth under a dramatic sunset sky"></div>
<h1 class="abs hero-title">Sculpting Land With<br><b>Precision And <span class="green">Power</span></b></h1>
<p class="abs hero-text">Pickens County's trusted land clearing, grading, and dump trailer specialists.</p>
<div class="abs btn btn-green" style="left:141px;top:465px;width:146px;height:41px;font-size:13px">Get A Free Quote</div>
<div class="abs btn btn-white" style="left:302px;top:465px;width:126px;height:41px;font-size:13px">View Services</div>
<div class="abs avatars" role="img" aria-label="Client portraits"><span></span><span></span><span style="background:linear-gradient(135deg,#8a4b3c,#d9b38c)"></span></div>
<div class="abs trust">Trusted More Than<br>5000+ Clients</div>

<!-- services -->
<div class="abs eyebrow" style="left:142px;top:728px">What We Do</div>
<h2 class="abs section-title" style="left:142px;top:756px"><span class="green">OUR</span> SERVICES</h2>
<p class="abs" style="left:545px;top:728px;width:515px;font-size:15px;line-height:21.5px;color:var(--muted)">Lorem ipsum dolor sit amet, consectetuer adipiscing elit, sedden nonummy nibh euismod tincidunt utter laoreet dolore magna aliquam erat volutpat. Ut wisi enim ad minim veniam.</p>

<div class="abs card" style="left:141px">
  <div class="photo" role="img" aria-label="Yellow excavator grading a site" style="background:linear-gradient(180deg,#9cc6e6 0%,#d6e3ea 45%,#e2b530 60%,#8a7a55 85%)"></div>
  <div class="tab">GRADING</div>
  <p>Lorem ipsum dolor sitting is amet consectetuer adipiscing elit, seddent diam nonummy nibh euismod there tincidunt ut laoreet dolore.</p>
  <div class="go"><svg width="10" height="12" viewBox="0 0 10 12"><path d="M2 1l5 5-5 5" fill="none" stroke="#4a9634" stroke-width="2"/></svg></div>
</div>
<div class="abs card" style="left:455px">
  <div class="photo" role="img" aria-label="Worker feeding a mulching machine" style="background:linear-gradient(135deg,#6b4a2c 0%,#d9652a 45%,#5a6d80 75%,#3a3a3a 100%)"></div>
  <div class="tab">MULCHING</div>
  <p>Lorem ipsum dolor sitting is amet consectetuer adipiscing elit, seddent diam nonummy nibh euismod there tincidunt ut laoreet dolore.</p>
  <div class="go"><svg width="10" height="12" viewBox="0 0 10 12"><path d="M2 1l5 5-5 5" fill="none" stroke="#4a9634" stroke-width="2"/></svg></div>
</div>
<div class="abs card" style="left:770px">
  <div class="photo" role="img" aria-label="Dump truck hauling soil at a quarry" style="background:linear-gradient(180deg,#c9ccc9 0%,#b9a98c 50%,#9c8a6c 100%)"></div>
  <div class="tab">HAULING</div>
  <p>Lorem ipsum dolor sitting is amet consectetuer adipiscing elit, seddent diam nonummy nibh euismod there tincidunt ut laoreet dolore.</p>
  <div class="go"><svg width="10" height="12" viewBox="0 0 10 12"><path d="M2 1l5 5-5 5" fill="none" stroke="#4a9634" stroke-width="2"/></svg></div>
</div>
<div class="abs btn btn-green" style="left:513px;top:1237px;width:173px;height:42px;font-size:12.5px;border-radius:3px">VIEW ALL SERVICES</div>

<!-- testimonials -->
<div class="abs testi-band"></div>
<div class="abs eyebrow" style="left:0;top:1448px;width:1200px;text-align:center">Testimonials</div>
<h2 class="abs section-title" style="left:0;top:1476px;width:1200px;text-align:center"><span class="green">WHAT OUR</span> CUSTOMERS SAY</h2>

<div class="abs t-card" style="left:141px">
  <div class="face" role="img" aria-label="Customer portrait"></div>
  <div class="name">Marcus Hale</div>
  <div class="stars">★★★★★</div>
  <p>Lorem ipsum dolor sitted there is amet, consectetuer adipiscing elit, seddened nonummy nibh euismod tincidunt utter laoreet dolore magna aliquam eratting volutpat. Ut wisi enim adden minim there is arent for veniam.</p>
  <svg class="quote" width="46" height="34" viewBox="0 0 46 34"><g fill="#5aa544"><circle cx="10" cy="24" r="10"/><path d="M1 24C1 12 6 5 15 2l2 3C11 8 8 13 8 20z"/><circle cx="34" cy="24" r="10"/><path d="M25 24C25 12 30 5 39 2l2 3C35 8 32 13 32 20z"/></g></svg>
</div>
<div class="abs t-card" style="left:614px">
  <div class="face" role="img" aria-label="Customer portrait"></div>
  <div class="name">Delia Brooks</div>
  <div class="stars">★★★★★</div>
  <p>Lorem ipsum dolor sitted there is amet, consectetuer adipiscing elit, seddened nonummy nibh euismod tincidunt utter laoreet dolore magna aliquam eratting volutpat. Ut wisi enim adden minim there is arent for veniam.</p>
  <svg class="quote" width="46" height="34" viewBox="0 0 46 34"><g fill="#5aa544"><circle cx="10" cy="24" r="10"/><path d="M1 24C1 12 6 5 15 2l2 3C11 8 8 13 8 20z"/><circle cx="34" cy="24" r="10"/><path d="M25 24C25 12 30 5 39 2l2 3C35 8 32 13 32 20z"/></g></svg>
</div>
<div class="abs arrow" style="left:79px;top:1644px;background:var(--white)"><svg width="10" height="12" viewBox="0 0 10 12"><path d="M7 1L2 6l5 5" fill="none" stroke="#222a33" stroke-width="2"/></svg></div>
<div class="abs arrow" style="left:1094px;top:1644px;background:var(--green)"><svg width="10" height="12" viewBox="0 0 10 12"><path d="M3 1l5 5-5 5" fill="none" stroke="#fff" stroke-width="2"/></svg></div>
<svg class="abs" style="left:553px;top:1818px" width="94" height="17" viewBox="0 0 94 17">
  <circle cx="8" cy="8.5" r="6" fill="#fff" stroke="#bbb"/>
  <rect x="29" y="1.5" width="36" height="14" rx="7" fill="#fff" stroke="#4a9634"/>
  <rect x="33" y="5" width="28" height="7" rx="3.5" fill="#4a9634"/>
  <circle cx="86" cy="8.5" r="6" fill="#fff" stroke="#bbb"/>
</svg>

<!-- contact -->
<div class="abs cta-box">
  <h3>READY TO SEE BRINDLE AND<br>FERN LLC IN ACTION?</h3>
  <p>Lorem ipsum dolor sitted there is amet, consectetuer there's adipiscing elit, seddened nonummy.</p>
  <div class="btn btn-green" style="position:absolute;left:37px;top:249px;width:166px;height:41px;font-size:13px;border-radius:3px">GET A FREE QUOTE</div>
</div>
<div class="abs form-box">
  <h2>GET IN <span>TOUCH</span></h2>
  <div class="field" style="top:138px;height:45px"><label>Full Name</label><div class="val">Enter your name</div></div>
  <div class="field" style="top:205px;height:45px"><label>Phone No</label><div class="val">123 456 7890</div></div>
  <div class="field" style="top:273px;height:45px"><label>Email Address</label><div class="val">info@brindleandfernllc.com</div></div>
  <div class="field" style="top:342px;height:126px"><label>Message</label><div class="val">Type your message here...</div></div>
  <div class="submit">SUBMIT NOW</div>
</div>

<!-- map -->
<div class="abs map" role="img" aria-label="Map of the north Georgia service area with marked job locations"></div>
<div class="abs map-title"><span class="green">OUR</span>&nbsp;SERVICE AREAS</div>

<!-- footer -->
<div class="abs footer"></div>
<div class="abs f-brand"><span class="mark"></span>Brindle and Fern LLC</div>

<div class="abs f-head" style="left:417px">QUICK LINKS</div>
<div class="abs f-link" style="left:417px;top:3275px">• Home</div>
<div class="abs f-link" style="left:417px;top:3307px">• Services</div>
<div class="abs f-link" style="left:417px;top:3338px">• Contact Us</div>

<div class="abs f-head" style="left:621px">FOLLOW US</div>
<div class="abs f-soc" style="left:621px;top:3280px"><i><b></b></i>Fernbook</div>
<div class="abs f-soc" style="left:621px;top:3319px"><i><b></b></i>Chirper</div>
<div class="abs f-soc" style="left:621px;top:3359px"><i><b></b></i>Snapgram</div>
<div class="abs f-soc" style="left:621px;top:3399px"><i><b></b></i>Worklink</div>

<div class="abs f-head" style="left:822px">CONTACT DETAILS</div>
<div class="abs f-ct" style="left:822px;top:3276px">
  <i><svg width="12" height="15" viewBox="0 0 12 15"><path d="M6 0a6 6 0 0 0-6 6c0 4.5 6 9 6 9s6-4.5 6-9a6 6 0 0 0-6-6zm0 8.3A2.3 2.3 0 1 1 6 3.7a2.3 2.3 0 0 1 0 4.6z" fill="#fff"/></svg></i>
  <div>Address<br>123, Building Name, Street City,<br>State XY 123456</div>
</div>
<div class="abs f-ct" style="left:822px;top:3345px">
  <i><svg width="13" height="13" viewBox="0 0 24 24"><path fill="#fff" d="M6.6 10.8a15 15 0 0 0 6.6 6.6l2.2-2.2c.3-.3.7-.4 1-.2 1.1.4 2.3.6 3.6.6.6 0 1 .4 1 1V20c0 .6-.4 1-1 1A17 17 0 0 1 3 4c0-.6.4-1 1-1h3.5c.6 0 1 .4 1 1 0 1.3.2 2.5.6 3.6.1.3 0 .7-.2 1z"/></svg></i>
  <div>Phone<br>(123) 456-7890</div>
</div>
<div class="abs f-ct" style="left:822px;top:3395px">
  <i><svg width="14" height="10" viewBox="0 0 14 10"><rect x=".5" y=".5" width="13" height="9" fill="none" stroke="#fff"/><path d="M.5.5L7 6 13.5.5" fill="none" stroke="#fff"/></svg></i>
  <div>Email<br>info@brindleandfernllc.com</div>
</div>

<div class="abs copy">Copyright © 2025 BRINDLE AND FERN LLC. All Rights Reserved.</div>

</body>
</html>
```